Modern two-sided business card for a general enterprise that improves the digital user experience.

Our company based in Switzerland covers all services of the digital customer relationship. We automate online ads to acquire new customers and program mobile apps for more efficient customer care in customer service. We employ specialists in marketing, business management, data science, graphic designers, copywriters, UI and programmers. The new business card is intended to show our comprehensive role and various offering of the entire customer journey.

Company Font: Futura
Main Color: # 283583
Secondary: #fcfaee (and gray variations)
Website: https://vup.ch

As little address information as possible: company name, employee, mobile, email, company web & company phone.

Target Market(s)

C-Level (CEO, CIO, CTO), Head Sales, Head Marketing & Head Customer Service

Industry/Entity Type

Digital Marketing, Online-Marketing, Analytics

Contact Information for Business Card

Requirements
Must have
• Company logo type ": vup" only on one side

```html
<!DOCTYPE html>
<html lang="en">
<head>
<meta charset="UTF-8">
<title>vup – Business Card</title>
<link href="https://fonts.googleapis.com/css2?family=Jost:wght@400;500&display=swap" rel="stylesheet">
<style>
  :root {
    --brand-blue: #283583;
    --card-white: #ffffff;
    --text-gray: #5a5a5a;
    --divider-blue: #5a67b0;
    --stage-dark: #2f2f2f;
    --stage-light: #4a4a4a;
  }
  * { margin: 0; padding: 0; box-sizing: border-box; }
  html, body {
    width: 1200px;
    height: 900px;
    overflow: hidden;
  }
  body {
    background: radial-gradient(ellipse at 50% 40%, var(--stage-light) 0%, var(--stage-dark) 70%);
    font-family: 'Jost', 'Futura', sans-serif;
    display: flex;
    align-items: center;
    justify-content: center;
    gap: 40px;
  }
  .card {
    width: 540px;
    height: 310px;
    border-radius: 3px;
    box-shadow: 0 18px 40px rgba(0,0,0,0.45);
    position: relative;
  }
  .card--front {
    background: var(--card-white);
    display: flex;
    align-items: center;
    justify-content: center;
  }
  .identity {
    text-align: right;
    padding-right: 18px;
    margin-top: -44px;
  }
  .identity__name {
    color: var(--brand-blue);
    font-size: 21px;
    font-weight: 500;
    letter-spacing: 0.2px;
    text-transform: uppercase;
    line-height: 1.1;
  }
  .identity__role {
    color: var(--text-gray);
    font-size: 13px;
    font-weight: 400;
    margin-top: 2px;
  }
  .divider {
    width: 1px;
    height: 84px;
    background: var(--divider-blue);
  }
  .contacts {
    list-style: none;
    padding-left: 18px;
    margin-top: 44px;
  }
  .contacts__item {
    display: flex;
    align-items: center;
    gap: 7px;
    color: var(--text-gray);
    font-size: 15px;
    line-height: 20px;
  }
  .contacts__icon {
    width: 11px;
    height: 11px;
    flex: none;
  }
  .card--back {
    background: var(--brand-blue);
    display: flex;
    align-items: center;
    justify-content: center;
  }
  .company-name {
    color: var(--card-white);
    font-size: 56px;
    font-weight: 500;
    letter-spacing: 4px;
    line-height: 1;
  }
</style>
</head>
<body>
  <section class="card card--front" aria-label="Business card front">
    <div class="identity">
      <p class="identity__name">Daniel Weber</p>
      <p class="identity__role">Director</p>
    </div>
    <div class="divider"></div>
    <ul class="contacts">
      <li class="contacts__item">
        <svg class="contacts__icon" viewBox="0 0 12 12" aria-hidden="true">
          <path d="M2.5 1 L4.5 1 L5.2 3.5 L4 4.5 Q5 7 7.5 8 L8.5 6.8 L11 7.5 L11 9.5 Q10.5 11 9 11 Q1 10 1 2.8 Q1 1.2 2.5 1 Z" fill="#283583"/>
        </svg>
        +41 (0) 44 310 45 67
      </li>
      <li class="contacts__item">
        <svg class="contacts__icon" viewBox="0 0 12 12" aria-hidden="true">
          <circle cx="4" cy="3.5" r="2.3" fill="#283583"/>
          <circle cx="8.5" cy="4.5" r="2" fill="#283583"/>
          <circle cx="5.5" cy="8.6" r="2.4" fill="#283583"/>
        </svg>
        CHE-204.771.356
      </li>
      <li class="contacts__item">
        <svg class="contacts__icon" viewBox="0 0 12 12" aria-hidden="true">
          <rect x="1" y="2.5" width="10" height="7" fill="none" stroke="#283583" stroke-width="1.3"/>
          <path d="M1 2.5 L6 6.5 L11 2.5" fill="none" stroke="#283583" stroke-width="1.3"/>
        </svg>
        info (at) vup.ch
      </li>
      <li class="contacts__item">
        <svg class="contacts__icon" viewBox="0 0 12 12" aria-hidden="true">
          <circle cx="6" cy="6" r="5" fill="none" stroke="#283583" stroke-width="1.2"/>
          <ellipse cx="6" cy="6" rx="2.2" ry="5" fill="none" stroke="#283583" stroke-width="1"/>
          <path d="M1 6 H11 M2 3.5 H10 M2 8.5 H10" stroke="#283583" stroke-width="1"/>
        </svg>
        www.vup.ch
      </li>
    </ul>
  </section>

  <section class="card card--back" aria-label="Business card back">
    <p class="company-name">vup</p>
  </section>
</body>
</html>
```